Website for 3d printing & other services

Hi, i'm after a website to sell my 3d printed automotive parts as well as sell my 3d printing services & other services.

There's a few things i need the website to have:

- Automatic 3d print quoting based on the file the client uploads to the website.
- Shop function where i can sell my custom automotive parts
- 3D printing technologies offered are SLA & FDM
- My business can offer 3d printing, 3d scanning, 3d cad design, cnc machining, steel fabrication, drafting services.

The color design is to suit my logo which is Black, orange & white.

Target Market(s)

3d printing, automotive, fabrication

Industry/Entity Type

General manufacturing & Custom automotive parts

Coding

Coded - Design and coding required

Number of Pages Required

5+ page

Requirements
Must have
• Automatic 3d print quoting. Shop for my printed parts.

```html
<!DOCTYPE html>
<html lang="en">
<head>
<meta charset="utf-8">
<title>Ferrowell Studio</title>
<link href="https://fonts.googleapis.com/css2?family=Krona+One&family=Roboto:wght@400;500;700&display=swap" rel="stylesheet">
<style>
:root{
  --orange:#f97a0e;
  --black:#0b0b0b;
  --ink:#1b1b1b;
  --text:#555a60;
  --white:#ffffff;
  --field:#eceff6;
  --card-shadow:0 2px 10px rgba(0,0,0,.09);
}
*{box-sizing:border-box;margin:0;padding:0}
html,body{width:1200px;height:5021px;overflow:hidden}
body{position:relative;background:var(--white);font-family:"Roboto",Arial,sans-serif;color:var(--text)}
.abs{position:absolute}
.display{font-family:"Krona One","Arial Black",sans-serif;color:var(--ink);text-transform:uppercase;letter-spacing:1px}
.btn{position:absolute;display:flex;align-items:center;justify-content:center;background:var(--orange);color:var(--white);font-size:14px;font-weight:500;border-radius:2px}
.rule{position:absolute;height:2px;width:80px;background:var(--orange);left:560px}
.center{left:0;width:1200px;text-align:center}
.lead{font-size:15px;line-height:32px}

/* header */
.topline{top:0;left:0;width:1200px;height:4px;background:var(--orange)}
.brand{top:64px;left:111px;font-family:"Roboto",Arial,sans-serif;font-weight:700;color:var(--orange);font-size:26px;line-height:32px;display:flex;align-items:center;gap:10px;white-space:nowrap}
.brand-mark{width:14px;height:14px;background:var(--orange)}
.btn-phone{background:var(--black)}
.nav{top:112px;left:405px;display:flex;align-items:center;font-size:14px;color:var(--ink);font-weight:500}
.nav span{margin-right:42px}
.nav svg{margin-right:12px}

/* hero */
.hero{top:185px;left:0;width:1200px;height:581px;background:linear-gradient(100deg,#1f7fc8 0%,#3a9be0 45%,#5aa9d8 70%,#1b3b5a 100%)}
.hero-welcome{top:300px;left:111px;font-size:34px;color:var(--white)}
.hero-title{top:356px;left:111px;font-size:47px;line-height:64px;color:var(--white)}
.hero-text{top:493px;left:111px;width:500px;font-size:15px;line-height:29px;color:var(--white)}

/* offer cards */
.offer-card{position:absolute;top:1114px;width:236px;height:312px;background:var(--white);box-shadow:var(--card-shadow)}
.offer-card .ph{position:absolute;top:6px;left:6px;right:6px;height:250px}
.offer-card p{position:absolute;top:282px;left:0;width:100%;text-align:center;font-size:15px;font-weight:500;color:var(--ink)}
.arrow{position:absolute;top:1467px;width:35px;height:35px;border-radius:50%;display:flex;align-items:center;justify-content:center}

/* technologies */
.tech-title{font-size:33px}
.tech-copy{font-size:15px;line-height:32px;width:450px}
.tech-img{position:absolute;border-radius:6px}

/* parts */
.parts{top:3043px;left:0;width:1200px;height:703px;background:linear-gradient(180deg,#fb7d10,#f67206)}
.part{position:absolute;top:3284px;width:230px;height:273px;background:var(--white);border-radius:4px}
.part .ph{position:absolute;left:40px;top:50px;width:150px;height:150px;border-radius:10px}
.part-meta{position:absolute;top:3578px;width:230px;text-align:center;color:var(--white)}
.part-meta .stars{font-size:11px;display:flex;justify-content:center;align-items:center;gap:6px}
.part-meta h4{font-size:15px;font-weight:700;margin-top:10px}
.part-meta b{display:block;font-size:19px;margin-top:10px}

/* quote */
.label{position:absolute;font-size:13px;color:var(--ink)}
.field{position:absolute;background:var(--field);font-size:13px;color:#777;padding-left:35px;display:flex;align-items:center;justify-content:space-between;padding-right:30px}

/* footer */
.footer{top:4662px;left:0;width:1200px;height:359px;background:var(--black)}
.foot-col{position:absolute;top:4734px;color:var(--white)}
.foot-col h5{font-family:"Krona One",sans-serif;font-size:18px;font-weight:400;margin-bottom:22px;letter-spacing:1px}
.foot-col li{list-style:none;font-size:15px;line-height:32.5px}
</style>
</head>
<body>

<header>
  <div class="abs topline"></div>
  <div class="abs brand"><span class="brand-mark"></span>Ferrowell Studio</div>
  <a class="btn" style="top:43px;left:768px;width:146px;height:43px">Get Started</a>
  <a class="btn btn-phone" style="top:43px;left:933px;width:154px;height:43px">+1 888 888 8888</a>
  <nav class="abs nav">
    <svg width="16" height="14" viewBox="0 0 16 14"><path d="M8 0 0 7h2v7h4V9h4v5h4V7h2z" fill="var(--orange)"/></svg>
    <span>About Us</span><span>Services</span><span>Custom Automotive Parts</span><span style="margin-right:30px">3D Printing Technologies</span>
    <svg width="16" height="14" viewBox="0 0 16 14"><path d="M0 0h3l1 2h12l-2 6H5zM5 10h9v1H5z" fill="var(--orange)"/><circle cx="6" cy="13" r="1" fill="var(--orange)"/><circle cx="13" cy="13" r="1" fill="var(--orange)"/></svg>
  </nav>
</header>

<section>
  <div class="abs hero" role="img" aria-label="3D printer nozzle printing a yellow part on a blue print bed"></div>
  <h2 class="abs display hero-welcome">Welcome to</h2>
  <h1 class="abs display hero-title">Ferrowell<br>Studio</h1>
  <p class="abs hero-text">I must explain to you how all this mistaken idea of denouncing pleasure and praising pain was born and I will give you a complete account of the system, and expound the actual teachings</p>
  <a class="btn" style="top:602px;left:111px;width:144px;height:37px">Get Started</a>
</section>

<section>
  <h2 class="abs display center" style="top:874px;font-size:35px">What We Offer</h2>
  <div class="rule" style="top:926px"></div>
  <p class="abs center lead" style="top:972px;left:150px;width:900px">I must explain to you how all this mistaken idea of denouncing pleasure and praising pain was born and I will give you a complete account of the system, and expound the actual teachings of the great explorer of the truth, the master-builder of human happiness. No one rejects, dislikes</p>
  <div class="offer-card" style="left:107px"><div class="ph" role="img" aria-label="3D printer printing a red lattice bowl" style="background:linear-gradient(160deg,#3b7fc4,#d8343a)"></div><p>3D Printing</p></div>
  <div class="offer-card" style="left:357px"><div class="ph" role="img" aria-label="3D scanning room with scanner equipment" style="background:linear-gradient(160deg,#dfe3e8,#9aa6b2)"></div><p>3D Scanning</p></div>
  <div class="offer-card" style="left:607px"><div class="ph" role="img" aria-label="CAD model of an engine on a monitor" style="background:linear-gradient(160deg,#4c79b0,#1e2e45)"></div><p>3D Cad Design</p></div>
  <div class="offer-card" style="left:857px"><div class="ph" role="img" aria-label="Sparks from steel being cut" style="background:linear-gradient(160deg,#5a3a28,#e8833a)"></div><p>Steel Fabrication</p></div>
  <div class="arrow" style="left:560px;background:var(--white)"><svg width="8" height="12" viewBox="0 0 8 12"><path d="M6 1 1 6l5 5" stroke="var(--ink)" stroke-width="2" fill="none"/></svg></div>
  <div class="arrow" style="left:604px;background:var(--orange)"><svg width="8" height="12" viewBox="0 0 8 12"><path d="m2 1 5 5-5 5" stroke="#fff" stroke-width="2" fill="none"/></svg></div>
</section>

<section>
  <h2 class="abs display center" style="top:1595px;font-size:35px">3D Printing Technologies</h2>
  <div class="rule" style="top:1659px"></div>
  <p class="abs center lead" style="top:1690px;left:150px;width:900px">I must explain to you how all this mistaken idea of denouncing pleasure and praising pain was born and I will give you a complete account of the system, and expound the actual teachings of the great explorer of the truth, the master-builder of human</p>

  <h3 class="abs display tech-title" style="top:1825px;left:111px">SLA</h3>
  <p class="abs tech-copy" style="top:1879px;left:111px">I must explain to you how all this mistaken idea of denouncing pleasure and praising pain was born and I will give you a complete account of the system, and expound the actual teachings of the great explorer of the truth, the master-builder of human happiness. No one rejects, dislikes, or avoids pleasure itself, because it is pleasure</p>
  <p class="abs tech-copy" style="top:2101px;left:111px">Nor again is there anyone who loves or pursues or desires to obtain pain of itself, because it is pain, but because occasionally circumstances occur in which toil</p>
  <a class="btn" style="top:2227px;left:111px;width:111px;height:41px">Read More</a>
  <div class="tech-img" role="img" aria-label="Hand adjusting a 3D printer frame" style="left:617px;top:1802px;width:470px;height:495px;background:linear-gradient(135deg,#e9e4de,#8a7a6a 55%,#2c2824)"></div>

  <div class="tech-img" role="img" aria-label="Nozzle printing a dark Y-shaped part on a print bed" style="left:111px;top:2400px;width:470px;height:495px;background:linear-gradient(160deg,#6e94ad,#2e4a60 60%,#1c2c3a)"></div>
  <h3 class="abs display tech-title" style="top:2421px;left:635px">FDM</h3>
  <p class="abs tech-copy" style="top:2477px;left:635px">I must explain to you how all this mistaken idea of denouncing pleasure and praising pain was born and I will give you a complete account of the system, and expound the actual teachings of the great explorer of the truth, the master-builder of human happiness. No one rejects, dislikes, or avoids pleasure itself, because it is pleasure</p>
  <p class="abs tech-copy" style="top:2699px;left:635px">Nor again is there anyone who loves or pursues or desires to obtain pain of itself, because it is pain, but because occasionally circumstances occur in which toil</p>
  <a class="btn" style="top:2825px;left:635px;width:111px;height:40px">Read More</a>
</section>

<section>
  <div class="abs parts"></div>
  <h2 class="abs display center" style="top:3126px;font-size:35px;color:var(--white)">My Custom Automotive Parts</h2>
  <div class="rule" style="top:3194px;background:rgba(255,255,255,.6)"></div>
  <p class="abs center" style="top:3226px;font-size:14.5px;color:var(--white)">I must explain to you how all this mistaken idea of denouncing pleasure and praising pain was born and I will give</p>

  <div class="part" style="left:111px">
    <svg class="abs" style="top:22px;right:16px" width="16" height="14" viewBox="0 0 16 14"><path d="M8 13 1.5 6.5A3.5 3.5 0 0 1 8 2a3.5 3.5 0 0 1 6.5 4.5z" stroke="var(--orange)" stroke-width="1.4" fill="none"/></svg>
    <div class="ph" role="img" aria-label="Black and white roller gear assembly" style="background:radial-gradient(circle,#555 0%,#e8e8e8 70%,#fff 100%)"></div>
    <div class="abs" style="left:14px;top:222px;width:204px;height:43px;background:var(--orange);border-radius:3px;color:#fff;font-size:14px;font-weight:500;display:flex;align-items:center;justify-content:space-between;padding:0 18px">Shop Now<svg width="14" height="12" viewBox="0 0 16 14"><path d="M0 0h3l1 2h12l-2 6H5z" fill="#fff"/><circle cx="6" cy="12" r="1.5" fill="#fff"/><circle cx="13" cy="12" r="1.5" fill="#fff"/></svg></div>
  </div>
  <div class="part" style="left:360px"><div class="ph" role="img" aria-label="Long black roller shaft" style="background:linear-gradient(135deg,#fff 30%,#333 50%,#fff 70%)"></div></div>
  <div class="part" style="left:610px"><div class="ph" role="img" aria-label="Black printer unit assembly with blue parts" style="background:radial-gradient(circle,#3a3f4a 0%,#8a8f98 55%,#fff 80%)"></div></div>
  <div class="part" style="left:859px"><div class="ph" role="img" aria-label="Scanner module with yellow label" style="background:radial-gradient(circle,#c9b640 0%,#444 50%,#fff 80%)"></div></div>

  <div class="part-meta" style="left:111px"><div class="stars">★★★★☆ <span>( 4 Reviews )</span></div><h4>Sed ut perspiciatis unde</h4><b>$ 20</b></div>
  <div class="part-meta" style="left:360px"><div class="stars">★★★★☆ <span>( 4 Reviews )</span></div><h4>Sed ut perspiciatis unde</h4><b>$ 20</b></div>
  <div class="part-meta" style="left:610px"><div class="stars">★★★★☆ <span>( 4 Reviews )</span></div><h4>Sed ut perspiciatis unde</h4><b>$ 20</b></div>
  <div class="part-meta" style="left:859px"><div class="stars">★★★★☆ <span>( 4 Reviews )</span></div><h4>Sed ut perspiciatis unde</h4><b>$ 20</b></div>
</section>

<section>
  <h2 class="abs display center" style="top:3845px;font-size:35px">Get A Quote</h2>
  <div class="rule" style="top:3902px"></div>
  <p class="abs center" style="top:3941px;font-size:14.5px">We are California's Premiere Speciality Firestopping &amp; Seismic Expansion Joint Contractor</p>

  <span class="label" style="top:4020px;left:179px">Full Name</span>
  <div class="field" style="top:4056px;left:179px;width:404px;height:48px">John<svg width="11" height="12" viewBox="0 0 11 12"><circle cx="5.5" cy="3" r="3" fill="#666"/><path d="M0 12a5.5 5 0 0 1 11 0z" fill="#666"/></svg></div>
  <span class="label" style="top:4020px;left:617px">Contact Number</span>
  <div class="field" style="top:4056px;left:617px;width:402px;height:48px">+1 888 888 8888<svg width="12" height="12" viewBox="0 0 12 12"><path d="M2 0h3l1 3-2 1a7 7 0 0 0 4 4l1-2 3 1v3a2 2 0 0 1-2 2A10 10 0 0 1 0 2a2 2 0 0 1 2-2z" fill="#666"/></svg></div>

  <span class="label" style="top:4136px;left:179px">Email Address</span>
  <div class="field" style="top:4171px;left:179px;width:404px;height:49px">jordanlee@mailbox.net<svg width="13" height="10" viewBox="0 0 13 10"><rect width="13" height="10" rx="1" fill="#666"/><path d="m1 1 5.5 4L12 1" stroke="#eceff6" fill="none"/></svg></div>
  <span class="label" style="top:4136px;left:617px">Upload Files Here</span>
  <div class="field" style="top:4171px;left:617px;width:402px;height:49px">Choose File<svg width="14" height="10" viewBox="0 0 14 10"><path d="M3.5 10a3.5 3.5 0 0 1 0-7 4 4 0 0 1 7.5 1 3 3 0 0 1 0 6z" fill="#666"/><path d="M7 8V4M5 6l2-2 2 2" stroke="#eceff6" fill="none"/></svg></div>

  <span class="label" style="top:4250px;left:179px">Comments</span>
  <div class="field" style="top:4285px;left:179px;width:840px;height:201px;align-items:flex-start;padding-top:22px">Your Message Goes Here.....<svg width="14" height="12" viewBox="0 0 14 12"><ellipse cx="5.5" cy="4.5" rx="5.5" ry="4" fill="#666"/><ellipse cx="9" cy="7.5" rx="5" ry="3.5" fill="#666"/></svg></div>

  <a class="btn" style="top:4519px;left:528px;width:144px;height:43px">Submit Here</a>
</section>

<footer>
  <div class="abs footer"></div>
  <div class="abs brand" style="top:4805px;font-size:30px;line-height:36px"><span class="brand-mark" style="width:18px;height:18px"></span>Ferrowell Studio</div>
  <div class="foot-col" style="left:427px"><h5>QUICK LINKS</h5><ul><li>Home</li><li>About Us</li><li>Our Services</li><li>3D Printing Technologies</li></ul></div>
  <div class="foot-col" style="left:688px"><h5>HELP LINKS</h5><ul><li>Our Products</li><li>Testimonials</li><li>Blogs</li><li>Contact Us</li></ul></div>
  <div class="foot-col" style="left:929px"><h5>FOLLOW US</h5><ul><li>Friendwall</li><li>Picstream</li><li>Chirper</li><li>Worknet</li></ul></div>
  <p class="abs center" style="top:4955px;font-size:14.5px;color:var(--white)">© 2023 Ferrowell Studio | All Rights Reserved.</p>
</footer>

</body>
</html>
```